Clean Plinth Ads Banner Design For A Finance Company

Hi,
We're a UK based finance company and are looking for new banner ads to use on the Plinth Display Network.
We want the end product to stand out by using strong, minimal design - ideally starting from a dark theme, although I'm open to ideas.
The copy should read:
'Fast Bridging Loans From 0.39% PM'
Once we have these designs agreed, we are looking to replicate them for other products, changing only the text on each ad - for example, 'commercial mortgage service you can rely on' or 'development finance service you can rely on'.
The colours used on our website are the following:
Black - #040303
Orange - #f79124
White - #ffffff
Grey - #ffffff
Example ads that I like - https://www.brimcastle.com/wp-content/uploads/2021/07/plinth-display-ads-example-2-final.png.webp
2 - https://quendrahub.com/wp-content/uploads/2020/03/fbdd56ba3bd16c7a8debb13a411de786.jpg

```html
<!DOCTYPE html>
<html lang="en">
<head>
<meta charset="utf-8">
<title>Arlo Finance – Fast Bridging Loans</title>
<link rel="stylesheet" href="https://fonts.googleapis.com/css2?family=Roboto:wght@400;500;700&display=swap">
<style>
  :root {
    --black: #040303;
    --panel: #0c0b0b;
    --orange: #f79124;
    --white: #ffffff;
    --rule: rgba(255,255,255,0.28);
  }
  * { margin: 0; padding: 0; box-sizing: border-box; }
  html, body {
    width: 1200px; height: 2400px; overflow: hidden;
    background: var(--black);
  }
  .banner {
    position: relative;
    width: 1200px; height: 2400px;
    background: var(--panel);
    font-family: "Roboto", Arial, sans-serif;
    color: var(--white);
    overflow: hidden;
  }
  .brand-name {
    position: absolute; top: 120px; left: 0; width: 100%;
    text-align: center;
    font-size: 120px; font-weight: 500; letter-spacing: -1px;
    color: var(--orange);
    line-height: 1;
  }
  .brand-rule {
    position: absolute; top: 378px; left: 180px;
    width: 840px; height: 3px;
    background: linear-gradient(90deg, transparent, var(--rule) 25%, var(--rule) 75%, transparent);
  }
  .product-icon {
    position: absolute; top: 500px; left: 524px;
    width: 152px; height: 152px;
  }
  .headline {
    position: absolute; top: 700px; left: 0; width: 100%;
    text-align: center;
    font-size: 98px; font-weight: 400; line-height: 120px;
  }
  .rate {
    position: absolute; top: 1040px; left: 0; width: 100%;
    text-align: center;
    font-size: 116px; font-weight: 700; line-height: 1;
    color: var(--orange);
  }
  .handshake-photo {
    position: absolute; top: 1350px; left: 0;
    width: 1200px; height: 560px;
    background:
      linear-gradient(180deg, var(--panel) 0%, transparent 22%, transparent 78%, var(--panel) 100%),
      linear-gradient(90deg, #1a1a1a 0%, #3c3c3c 30%, #9a9a9a 50%, #3c3c3c 70%, #1a1a1a 100%);
  }
  .cta {
    position: absolute; top: 1940px; left: 340px;
    width: 520px; height: 164px;
    border-radius: 82px;
    background: var(--orange);
    color: var(--black);
    font-size: 52px; font-weight: 700; letter-spacing: 1px;
    display: flex; align-items: center; justify-content: center;
  }
</style>
</head>
<body>
  <main class="banner">
    <div class="brand-name">Arlo Finance</div>
    <div class="brand-rule"></div>

    <svg class="product-icon" viewBox="0 0 38 38" fill="none" stroke="#f79124" stroke-width="2" stroke-linejoin="round" stroke-linecap="round" aria-hidden="true">
      <rect x="7" y="2" width="26" height="14" rx="1"/>
      <rect x="5" y="5" width="26" height="14" rx="1" fill="#0c0b0b"/>
      <circle cx="18" cy="12" r="3"/>
      <path d="M2 24h6l5 4h9a2 2 0 0 1 0 4h-8"/>
      <path d="M22 30l10-6a2 2 0 0 1 3 3l-11 9H2"/>
    </svg>

    <h1 class="headline">Fast<br>Bridging Loans<br>From</h1>
    <div class="rate">0.39% PM</div>

    <div class="handshake-photo" role="img" aria-label="Black and white photo of two business people in suits shaking hands"></div>

    <div class="cta">LEARN MORE</div>
  </main>
</body>
</html>
```